EPS Packaging Infographic

We need two infographics focus on EPS packaging.

I've attached the copy as well as some of our other infographics to give you an idea of our style.

```html
<!DOCTYPE html>
<html lang="en">
<head>
<meta charset="utf-8">
<title>PS Bans vs. Curbside Collection</title>
<link rel="stylesheet" href="https://fonts.googleapis.com/css2?family=Bebas+Neue&family=Source+Sans+3:wght@400&display=swap">
<style>
  :root {
    --brown: #5e2d1e;
    --steel: #5b8ba8;
    --panel: #5e8eaa;
    --white: #ffffff;
    --label: #4d4d4d;
    --leader: #555555;
    --orange: #f3a223;
    --olive: #9a9837;
    --slate: #5689a3;
    --yellow: #f1d51b;
    --navy: #1c5470;
    --hole: #f2f3f5;
  }
  * { margin: 0; padding: 0; box-sizing: border-box; }
  html, body { width: 849px; height: 1200px; overflow: hidden; background: var(--white); }
  .infographic { position: relative; width: 849px; height: 1200px; overflow: hidden; background: var(--white); }
  .headline, .chart { position: absolute; left: 0; top: 0; }
  .headline text, .chart-title { font-family: "Bebas Neue", "Oswald", sans-serif; }
  .facts {
    position: absolute; left: 28px; top: 303px; width: 790px; height: 292px;
    background: var(--panel); border-radius: 16px;
    padding: 19px 52px 0 40px;
    color: var(--white);
    font-family: "Source Sans 3", "PT Sans", sans-serif; font-size: 23px; line-height: 27px;
    list-style: none;
  }
  .facts li { margin-bottom: 7.5px; }
  .facts li::before { content: "\2022\00a0"; }
  .chart-label { font-family: "Bebas Neue", "Oswald", sans-serif; font-size: 23px; fill: var(--label); }
  .leader { fill: none; stroke: var(--leader); stroke-width: 1.2; }
  .slice { stroke: var(--white); stroke-width: 4; }
  .brand {
    position: absolute; right: 40px; top: 1150px;
    font-family: "Source Sans 3", "PT Sans", sans-serif; font-size: 15px; line-height: 18px;
    color: var(--label); text-align: right;
  }
</style>
</head>
<body>
<main class="infographic">
  <svg class="headline" width="849" height="290" viewBox="0 0 849 290" aria-label="PS Bans vs. Curbside Collection">
    <text x="36" y="104" font-size="112" fill="var(--brown)" textLength="284" lengthAdjust="spacingAndGlyphs">PS BANS</text>
    <text x="36" y="183" font-size="108" fill="var(--steel)" textLength="88" lengthAdjust="spacingAndGlyphs">VS.</text>
    <text x="36" y="274" font-size="112" fill="var(--brown)" textLength="772" lengthAdjust="spacingAndGlyphs">CURBSIDE COLLECTION</text>
  </svg>

  <ul class="facts">
    <li>Nearly 300 Drop Off Locations</li>
    <li>82 Curbside Programs</li>
    <li>More than 50 Special Collection Events/Year</li>
    <li>20 National Mail Back Locations</li>
    <li>146 local governments – counties, cities and towns – in 15 states, including the District of Columbia, that have adopted ordinances to reduce or eliminate the consumption of food-service EPS. These ordinances covered 6.8 percent of the U.S. population.</li>
  </ul>

  <svg class="chart" width="849" height="1200" viewBox="0 0 849 1200">
    <text class="chart-title" x="36" y="682" font-size="52" fill="var(--steel)" textLength="774" lengthAdjust="spacingAndGlyphs">THE FIVE STATES WITH THE MOST EPS ORDINANCES</text>

    <g class="donut">
      <path class="slice" fill="var(--orange)" transform="translate(4 3)" d="M433 704 A216 216 0 1 1 247.5 1030.6 L364.3 961 A80 80 0 1 0 433 840 Z"/>
      <path class="slice" fill="var(--olive)" d="M271.5 1016.3 A188 188 0 0 1 246.1 899.8 L351.5 911.2 A82 82 0 0 0 362.6 962 Z"/>
      <path class="slice" fill="var(--slate)" d="M264 901.8 A170 170 0 0 1 277 852.4 L357.7 887.4 A82 82 0 0 0 351.5 911.2 Z"/>
      <path class="slice" fill="var(--yellow)" d="M288 857.2 A158 158 0 0 1 308.8 822.3 L368.5 869.3 A82 82 0 0 0 357.7 887.4 Z"/>
      <path class="slice" fill="var(--navy)" d="M315.1 827.2 A150 150 0 0 1 337.7 804.2 L380.9 856.7 A82 82 0 0 0 368.5 869.3 Z"/>
      <path class="slice" fill="var(--brown)" d="M313.6 774.8 A188 188 0 0 1 433 732 L433 838 A82 82 0 0 0 380.9 856.7 Z"/>
      <circle cx="435" cy="922" r="79" fill="var(--hole)" stroke="#e4e6ea" stroke-width="2"/>
    </g>

    <g class="labels">
      <polyline class="leader" points="578,776 627,732 655,732"/>
      <text class="chart-label" x="660" y="740">CALIFORNIA, 97</text>

      <polyline class="leader" points="310,718 344,718 368,760"/>
      <text class="chart-label" x="302" y="726" text-anchor="end">REST OF THE U.S., 16</text>

      <polyline class="leader" points="258,774 284,774 324,808"/>
      <text class="chart-label" x="250" y="782" text-anchor="end">MAINE, 5</text>

      <polyline class="leader" points="236,820 292,844"/>
      <text class="chart-label" x="216" y="824" text-anchor="end">NEW YORK, 6</text>

      <polyline class="leader" points="218,866 278,882"/>
      <text class="chart-label" x="194" y="874" text-anchor="end">FLORIDA, 7</text>

      <polyline class="leader" points="194,978 268,968"/>
      <text class="chart-label" x="182" y="986" text-anchor="end">MASSACHUSETTS, 15</text>
    </g>
  </svg>

  <p class="brand">Foam Pack Council</p>
</main>
</body>
</html>
```